International Travel Technology R&D business needs a wordpress website

We are a start up team of initially 2 individuals but plan to grow our team quickly, we have deep experience in travel technology. Our goal is to provide next generation technology research and development on behalf of our clients who are leading players in the travel technology industry. Attached our logos.

Target Market(s)

Travel Technology companies

Industry/Entity Type

Travel Industry

Coding

Coded - Design and coding required

Font styles to use
Sans Serif

Requirements
Must have
• Make use of our logo and colour scheme in the attached. Has to have a sense of adventure/ stepping into the unknown but equally must convey a sense of professionalism , we are a safe pair of hands. Sample themes are in the attachment .
Nice to have
• We have identified a theme on layoutbazaar which we feel would be inspirational. We hahe attached them to help in the design as inspiration.
Should not have
• images of airplanes , hotels etc, we want to project a future image.

```html
<!DOCTYPE html>
<html lang="en">
<head>
<meta charset="utf-8">
<title>Voyage Forge Labs</title>
<link rel="stylesheet" href="https://fonts.googleapis.com/css2?family=Michroma&family=Open+Sans:wght@400;600;700&family=PT+Serif&display=swap">
<style>
:root{
  --accent:#1ea3e0;
  --ink:#222;
  --muted:#8a8a8a;
  --logo-green:#5cb84a;
  --band-grey:#efefef;
  --footer:#2b2b2b;
  --footer-deep:#1f1f1f;
  --footer-text:#8c8c8c;
  --white:#fff;
}
*{margin:0;padding:0;box-sizing:border-box}
html,body{width:688px;height:1200px;overflow:hidden}
body{position:relative;background:var(--white);font-family:'Open Sans',sans-serif;color:var(--ink)}
.abs{position:absolute}
.display{font-family:'Michroma',sans-serif;letter-spacing:1.5px}
.serif{font-family:'PT Serif',serif}

/* header */
.site-header{left:0;top:0;width:688px;height:42px;background:var(--white)}
.brand{left:142px;top:11px;display:flex;align-items:center;gap:6px}
.brand-mark{width:20px;height:20px;border-radius:50%;background:var(--accent)}
.brand-name{font-size:10px;font-weight:700;color:var(--accent);letter-spacing:1px}
.nav{left:330px;top:16px;display:flex;gap:22px;font-size:7px;color:#444}

/* hero */
.hero{left:0;top:42px;width:688px;height:188px;background:linear-gradient(180deg,#4f8fbf 0%,#8fbcd9 45%,#b9c4c4 68%,#8c8278 100%)}
.hero-title{left:142px;top:110px;font-family:'Michroma',sans-serif;font-size:34px;color:rgba(255,255,255,.85);letter-spacing:-1px}
.hero-sub{left:143px;top:154px;font-size:6.5px;font-weight:600;color:#7a8590;line-height:9px}
.dots{left:327px;top:213px;display:flex;gap:3px}
.dots span{width:5px;height:5px;border-radius:50%;border:1px solid #222;background:var(--white)}
.dots span.on{background:#222}

/* section headings */
.section-title{left:0;width:688px;text-align:center;font-size:13px;color:var(--ink)}

/* features */
.feature{width:90px;text-align:center}
.feature svg{display:block;margin:0 auto 8px}
.feature h3{font-family:'PT Serif',serif;font-weight:400;font-size:7px;letter-spacing:.3px;margin-bottom:4px}
.feature p{font-size:4.8px;line-height:6.2px;color:var(--muted)}

/* services band */
.services-band{left:0;top:398px;width:688px;height:225px;background:linear-gradient(180deg,#bcd9e8 0%,#a9c6d6 40%,#90aab8 100%)}
.services-panel{left:154px;top:422px;width:378px;height:178px;background:rgba(255,255,255,.22)}
.services-frame{left:162px;top:429px;width:362px;height:165px;border:1px solid rgba(255,255,255,.8)}
.services-heading{left:169px;top:458px;font-size:14px;line-height:17px;color:var(--white)}
.services-intro{left:167px;top:500px;width:100px;font-size:4.8px;line-height:7.3px;color:var(--white)}
.services-divider{left:278px;top:452px;width:1px;height:120px;background:rgba(255,255,255,.8)}
.service{width:100px}
.service svg{position:absolute;left:-18px;top:-1px}
.service h4{font-family:'PT Serif',serif;font-weight:400;font-size:6.5px;color:#333;margin-bottom:4px}
.service p{font-size:4.6px;line-height:7.2px;color:var(--white)}

/* cards */
.card{width:128px;text-align:center}
.card .photo{width:128px;height:89px}
.card h3{font-family:'PT Serif',serif;font-weight:400;font-size:7px;margin:12px 0 5px}
.card p{font-size:4.8px;line-height:7.6px;color:var(--muted);padding:0 5px}
.btn{display:inline-block;margin-top:8px;width:49px;height:14px;line-height:14px;background:var(--accent);color:var(--white);font-size:4.8px;font-weight:700;letter-spacing:.3px}

/* partners */
.partners-band{left:0;top:882px;width:688px;height:147px;background:var(--band-grey)}
.partners-box{left:143px;top:942px;width:402px;height:55px;border:1px solid #ccc;display:flex;align-items:center}
.partner{flex:1;text-align:center;font-size:6.5px;font-weight:700;color:#3a7fb5;border-right:1px solid #ccc;line-height:26px}
.partner:last-child{border-right:0}

/* footer */
.site-footer{left:0;top:1029px;width:688px;height:147px;background:var(--footer)}
.footer-col h4{font-family:'PT Serif',serif;font-weight:400;font-size:7.5px;color:var(--white);margin-bottom:7px}
.footer-col p{font-size:4.5px;line-height:7.2px;color:var(--footer-text)}
.footer-col p b{color:var(--white);font-weight:600}
.socials{display:flex;gap:7px;margin-top:14px}
.socials span{width:7px;height:7px;border-radius:50%;background:var(--footer-text)}
.field{width:93px;height:12px;background:var(--white);font-size:4px;color:#888;padding:3px 5px}
.field.tall{height:29px;margin-top:6px}
.send{margin-top:6px;width:48px;height:11px;line-height:11px;background:var(--accent);color:var(--white);font-size:4.3px;font-weight:700;text-align:center}
.copyright{left:0;top:1176px;width:688px;height:24px;background:var(--footer-deep);text-align:center;font-size:5px;line-height:24px;color:var(--footer-text)}
</style>
</head>
<body>

<header class="site-header abs">
  <div class="brand abs"><span class="brand-mark"></span><span class="brand-name">VOYAGE FORGE LABS</span></div>
  <nav class="nav abs"><span>Home</span><span>Features</span><span>Portfolio</span><span>Service</span><span>Contact</span></nav>
</header>

<section class="hero abs" role="img" aria-label="Hazy city skyline under a blue cloudy sky"></section>
<div class="hero-title abs">EXERCITATION</div>
<p class="hero-sub abs">Sed do eiusmod tempor incididunt ut labore et dolore magna aliqua.<br>Ut enim ad minim veniam, quis nostrud</p>
<div class="dots abs"><span class="on"></span><span></span><span></span><span></span><span></span></div>

<h2 class="section-title display abs" style="top:256px">EXERCITATION</h2>

<div class="feature abs" style="left:153px;top:298px">
  <svg width="30" height="26" viewBox="0 0 30 26" fill="none" stroke="#1ea3e0" stroke-width="1.4"><rect x="2" y="2" width="26" height="17" rx="1"/><path d="M11 24h8M15 19v5M7 14l5-5 4 3 7-6"/></svg>
  <h3>EIUSMOD TEMPOR</h3>
  <p>Sed do eiusmod tempor incidi-dunt ut labore et dolore magna aliqua ut enim ad minimvniam, quis nostrud</p>
</div>
<div class="feature abs" style="left:251px;top:298px">
  <svg width="30" height="26" viewBox="0 0 30 26" fill="none" stroke="#1ea3e0" stroke-width="1.4"><rect x="8" y="2" width="14" height="21" rx="1"/><path d="M11 7h8M11 11h8M11 15h5M24 8v14"/></svg>
  <h3>EIUSMOD TEMPOR</h3>
  <p>Sed do eiusmod tempor incidi-dunt ut labore et dolore magna aliqua ut enim ad minimvniam, quis nostrud</p>
</div>
<div class="feature abs" style="left:347px;top:298px">
  <svg width="30" height="26" viewBox="0 0 30 26" fill="none" stroke="#1ea3e0" stroke-width="1.4"><path d="M9 19V12a6 6 0 0 1 12 0v7H9zM7 19h16M13 22h4M4 9a11 11 0 0 1 4-5M26 9a11 11 0 0 0-4-5"/></svg>
  <h3>EIUSMOD TEMPOR</h3>
  <p>Sed do eiusmod tempor incidi-dunt ut labore et dolore magna aliqua ut enim ad minimvniam, quis nostrud</p>
</div>
<div class="feature abs" style="left:443px;top:298px">
  <svg width="30" height="26" viewBox="0 0 30 26" fill="none" stroke="#1ea3e0" stroke-width="1.4"><circle cx="15" cy="15" r="8"/><path d="M15 15V10M15 15l3 2M12 4h6M15 4v3M6 8l2 2M24 8l-2 2"/></svg>
  <h3>EIUSMOD TEMPOR</h3>
  <p>Sed do eiusmod tempor incidi-dunt ut labore et dolore magna aliqua ut enim ad minimvniam, quis nostrud</p>
</div>

<section class="services-band abs" role="img" aria-label="Blurred aerial view of a city in pale blue tones"></section>
<div class="services-panel abs"></div>
<div class="services-frame abs"></div>
<h2 class="services-heading display abs">OUR<br>SERVICES</h2>
<p class="services-intro abs">Sed do eiusmod tempor incididunt ut labore et dolore magna aliqua. Ut enim ad minim veniam, quis nostrud exercita-tion ullamco laboris nisi ut aliquip ex ea</p>
<div class="services-divider abs"></div>

<div class="service abs" style="left:309px;top:452px">
  <svg width="12" height="12" viewBox="0 0 12 12" fill="#333"><circle cx="6" cy="6" r="2"/><circle cx="2" cy="2" r="1.3"/><circle cx="10" cy="2" r="1.3"/><circle cx="2" cy="10" r="1.3"/><circle cx="10" cy="10" r="1.3"/></svg>
  <h4>EIUSMOD TEMPOR</h4>
  <p>Sed do eiusmod tempor incididunt ut labore et dolore magna aliqua. Ut enim ad minim veniam, quis nostrud exercita-tion ullamco laboris nisi ut aliquip ex ea commodo consequat. Duis aute irure</p>
</div>
<div class="service abs" style="left:423px;top:452px">
  <svg width="13" height="12" viewBox="0 0 13 12" fill="none" stroke="#333"><rect x="1" y="1" width="11" height="9"/><circle cx="5" cy="5" r="1.5"/></svg>
  <h4>EIUSMOD TEMPOR</h4>
  <p>Sed do eiusmod tempor incididunt ut labore et dolore magna aliqua. Ut enim ad minim veniam, quis nostrud exercita-tion ullamco laboris nisi ut aliquip ex ea commodo consequat. Duis aute irure</p>
</div>
<div class="service abs" style="left:309px;top:522px">
  <svg width="12" height="12" viewBox="0 0 12 12" fill="none" stroke="#333"><circle cx="5" cy="4" r="2.5"/><path d="M1 11c0-3 2-4 4-4M7 8h4v3H7z"/></svg>
  <h4>EIUSMOD TEMPOR</h4>
  <p>Sed do eiusmod tempor incididunt ut labore et dolore magna aliqua. Ut enim ad minim veniam, quis nostrud exercita-tion ullamco laboris nisi ut aliquip ex ea commodo consequat. Duis aute irure</p>
</div>
<div class="service abs" style="left:423px;top:522px">
  <svg width="13" height="12" viewBox="0 0 13 12" fill="none" stroke="#333" stroke-width="1.2"><circle cx="9" cy="2" r="1.3"/><path d="M3 5l4-1 2 3-3 4M7 7l-4 4M1 3h3M0 6h3"/></svg>
  <h4>EIUSMOD TEMPOR</h4>
  <p>Sed do eiusmod tempor incididunt ut labore et dolore magna aliqua. Ut enim ad minim veniam, quis nostrud exercita-tion ullamco laboris nisi ut aliquip ex ea commodo consequat. Duis aute irure</p>
</div>

<h2 class="section-title display abs" style="top:648px">QUIS NOSTRUD</h2>

<article class="card abs" style="left:142px;top:686px">
  <div class="photo" role="img" aria-label="Pedestrians crossing a rainy street under umbrellas" style="background:linear-gradient(160deg,#9a9a98,#4a4a4a)"></div>
  <h3>NOSTRUD EXERCITATION</h3>
  <p>Sed do eiusmod tempor incididunt ut labore et dolore magna aliqua. Ut enim ad minim veniam, quis nostrud exercitation ullamco laboris nisi ut aliquip ex ea commodo consequat.</p>
  <span class="btn">VIEW MORE</span>
</article>
<article class="card abs" style="left:280px;top:686px">
  <div class="photo" role="img" aria-label="Soft focus tower rising above a city" style="background:linear-gradient(180deg,#d9e3e6,#a9b3b2)"></div>
  <h3>NOSTRUD EXERCITATION</h3>
  <p>Sed do eiusmod tempor incididunt ut labore et dolore magna aliqua. Ut enim ad minim veniam, quis nostrud exercitation ullamco laboris nisi ut aliquip ex ea commodo consequat.</p>
  <span class="btn">VIEW MORE</span>
</article>
<article class="card abs" style="left:418px;top:686px">
  <div class="photo" role="img" aria-label="Looking up at dark office towers" style="background:linear-gradient(160deg,#3e5b72,#1c3345)"></div>
  <h3>NOSTRUD EXERCITATION</h3>
  <p>Sed do eiusmod tempor incididunt ut labore et dolore magna aliqua. Ut enim ad minim veniam, quis nostrud exercitation ullamco laboris nisi ut aliquip ex ea commodo consequat.</p>
  <span class="btn">VIEW MORE</span>
</article>

<section class="partners-band abs"></section>
<h2 class="section-title display abs" style="top:908px">VOLUPTATE VELIT</h2>
<div class="partners-box abs">
  <span class="partner">Pelangi</span>
  <span class="partner">Skyward Tours</span>
  <span class="partner">Coastline 9</span>
  <span class="partner">Summit Trails</span>
  <span class="partner">Farview Trips</span>
</div>

<footer class="site-footer abs">
  <div class="footer-col abs" style="left:142px;top:28px;width:90px">
    <h4>EIUSMOD TEMPOR</h4>
    <p>We would love to hear your stories and answer any questions you might have. Please drop us a line using any of these methods.</p>
    <p style="margin-top:6px">E-mail: hello@voyageforgelabs.com</p>
    <div class="socials" aria-label="Social links"><span></span><span></span><span></span><span></span><span></span></div>
  </div>
  <div class="footer-col abs" style="left:246px;top:28px;width:104px">
    <h4>EIUSMOD TEMPOR</h4>
    <p><b>consectetur adipiscing elit</b><br>Lorem ipsum dolor sit amet, consectetur adipiscing elit. Donec sed auctor elit.</p>
    <p style="margin-top:7px"><b>consectetur adipiscing elit</b><br>Lorem ipsum dolor sit amet, consectetur adipiscing elit. Donec sed auctor elit.</p>
    <p style="margin-top:7px"><b>consectetur adipiscing elit</b><br>Lorem ipsum dolor sit amet, consectetur adipiscing elit. Donec sed auctor elit.</p>
  </div>
  <div class="footer-col abs" style="left:366px;top:28px;width:80px">
    <h4>EIUSMOD TEMPOR</h4>
    <p>Consectetur<br>Adipiscsed do<br>Eiusmod tempor<br>Incididunt ut labore<br>Dolore magna<br>Aliquaad<br>Minim veniam, quis<br>Nostrud exercitation<br>Ullamco laboris nisi<br>Aliquip ex ea com-</p>
  </div>
  <div class="footer-col abs" style="left:452px;top:28px;width:96px">
    <h4>CONTACT US</h4>
    <div class="field">YOUR E-MAIL...</div>
    <div class="field tall">YOUR TEXT...</div>
    <div class="send">SEND MESSAGE</div>
  </div>
</footer>
<div class="copyright abs">© Copyright 2016 Commodo consequat</div>

</body>
</html>
```